Law Firm Business Card

This is a business card for a law firm that serves US military and veterans.

The card must have ONLY the following (we want an uncluttered look):

- Company logo (PNG, GIF, JPEG copies uploaded)
- A tagline reading: "a law firm for service members and veterans"
- My name and title: "Martin Okello" and "Attorney"
- My email: "martin.okello@harborlinecounsel.com"
- My number: "855-FILE-NOW (345-3669)"

We are looking for a clean, simple layout with only the above information, likely printed on a bright white cotton stock. The font of our logo is DIN 1451, and the font used on our website is Helvetica Neue. The color of our logo is #336699, and we probably want the tagline in that color also, and my contact information in a dark grey. Please review our website at www.harborlinecounsel.com to ensure your card design complements our website style.

Thanks and we look forward to seeing your submissions.

A few notes:

- Two-sided submissions are ok
- Please don't add graphics (scales of justice, judges hammer, etc)

```html
<!DOCTYPE html>
<html lang="en">
<head>
<meta charset="utf-8">
<title>Harborline Counsel – Business Card</title>
<link rel="stylesheet" href="https://fonts.googleapis.com/css2?family=Barlow+Semi+Condensed:wght@500;600&family=Roboto:wght@300;400;700&display=swap">
<style>
  :root {
    --brand-blue: #336699;
    --band-blue: #2f67a8;
    --card-white: #ffffff;
    --text-dark: #4a4a4a;
    --text-mid: #8a8a8a;
    --backdrop: #e9e9ec;
    --rule-grey: #e2e2e2;
  }
  * { box-sizing: border-box; margin: 0; padding: 0; }
  html, body {
    width: 1200px;
    height: 800px;
    overflow: hidden;
    background: var(--backdrop);
  }
  .canvas {
    position: relative;
    width: 1200px;
    height: 800px;
    display: flex;
    align-items: center;
    justify-content: center;
  }
  .business-card {
    position: relative;
    width: 840px;
    height: 480px;
    background: var(--card-white);
    box-shadow: 0 10px 30px rgba(0,0,0,0.12);
    overflow: hidden;
  }
  .wordmark {
    position: absolute;
    top: 104px;
    left: 270px;
    width: 510px;
    text-align: center;
    white-space: nowrap;
    font-family: "Barlow Semi Condensed", sans-serif;
    font-weight: 600;
    font-size: 58px;
    line-height: 1;
    letter-spacing: 1px;
    color: var(--brand-blue);
    text-transform: uppercase;
  }
  .tagline-band {
    position: absolute;
    top: 182px;
    left: 0;
    width: 100%;
    height: 46px;
    background: var(--band-blue);
    display: flex;
    align-items: center;
    justify-content: flex-end;
    padding-right: 62px;
  }
  .tagline {
    font-family: "Barlow Semi Condensed", sans-serif;
    font-weight: 500;
    font-size: 28px;
    letter-spacing: 0.5px;
    white-space: nowrap;
    color: var(--card-white);
    text-transform: uppercase;
  }
  .person {
    position: absolute;
    top: 258px;
    left: 60px;
    font-family: "Roboto", sans-serif;
  }
  .person-name {
    font-size: 30px;
    letter-spacing: 0.5px;
    color: var(--text-dark);
    text-transform: uppercase;
  }
  .person-name .first { font-weight: 700; }
  .person-name .last { font-weight: 300; }
  .person-title {
    margin-top: 2px;
    font-size: 17px;
    font-weight: 300;
    letter-spacing: 1px;
    color: var(--text-mid);
    text-transform: uppercase;
  }
  .contact {
    position: absolute;
    top: 330px;
    left: 420px;
    padding-left: 16px;
    border-left: 1px solid var(--rule-grey);
    font-family: "Roboto", sans-serif;
    color: var(--text-dark);
  }
  .contact-line {
    display: flex;
    align-items: center;
    gap: 12px;
    height: 34px;
    white-space: nowrap;
  }
  .contact-icon { width: 16px; height: 16px; fill: var(--text-dark); flex: none; }
  .phone-main { font-size: 20px; font-weight: 700; }
  .phone-digits { font-size: 18px; font-weight: 400; color: var(--text-mid); margin-left: 6px; }
  .email { font-size: 18px; font-weight: 400; color: var(--text-mid); }
</style>
</head>
<body>
<main class="canvas">
  <article class="business-card">
    <div class="wordmark">Harborline Counsel</div>

    <div class="tagline-band">
      <p class="tagline">A law firm for service members and veterans</p>
    </div>

    <section class="person">
      <h1 class="person-name"><span class="first">Martin</span> <span class="last">Okello</span></h1>
      <p class="person-title">Attorney</p>
    </section>

    <section class="contact">
      <div class="contact-line">
        <svg class="contact-icon" viewBox="0 0 24 24" aria-hidden="true">
          <path d="M6.6 10.8a15.1 15.1 0 0 0 6.6 6.6l2.2-2.2a1 1 0 0 1 1-.25 11.4 11.4 0 0 0 3.6.57 1 1 0 0 1 1 1V20a1 1 0 0 1-1 1A17 17 0 0 1 3 4a1 1 0 0 1 1-1h3.5a1 1 0 0 1 1 1c0 1.25.2 2.45.57 3.6a1 1 0 0 1-.25 1z"/>
        </svg>
        <span><span class="phone-main">855-FILE-NOW</span><span class="phone-digits">(345-3669)</span></span>
      </div>
      <div class="contact-line">
        <svg class="contact-icon" viewBox="0 0 24 24" aria-hidden="true">
          <path d="M2 5h20v14H2z M4 7v.4l8 5.2 8-5.2V7z" fill-rule="evenodd"/>
        </svg>
        <span class="email">martin.okello@harborlinecounsel.com</span>
      </div>
    </section>
  </article>
</main>
</body>
</html>
```